Chiro Card
Bright Path Chiropractic & Wellness
Project: Chiro Card
Chiro Card -
Creative Brief
Simple
Marcus Hale
Chiropractor
812 Orvale Ave, Suite K Corbin Falls, Tx. 78245
corbinfallsspine@mailvane.com
www.corbinfallsspine.com
Please do not include my email address on the business card.

```html
<!DOCTYPE html>
<html lang="en">
<head>
<meta charset="utf-8">
<title>Bright Path Chiropractic &amp; Wellness – Business Card</title>
<link href="https://fonts.googleapis.com/css2?family=Cinzel:wght@700&family=Arimo:wght@400&family=Tinos:wght@400&display=swap" rel="stylesheet">
<style>
  :root {
    --bg: #e9e6e1;
    --card-white: #ffffff;
    --brand-green: #3c9a3a;
    --light-green: #9cc93b;
    --navy: #1f4f7a;
    --deep-navy: #12395d;
    --mid-blue: #2b6a9b;
    --name-blue: #2a5f93;
    --text-white: #ffffff;
    --soft-white: rgba(255,255,255,0.82);
  }
  * { margin: 0; padding: 0; box-sizing: border-box; }
  html, body { width: 1200px; height: 799px; overflow: hidden; }
  body { background: var(--bg); position: relative; font-family: "Arimo", Arial, sans-serif; }

  .card {
    position: absolute;
    width: 600px; height: 345px;
    border-radius: 22px;
    overflow: hidden;
    box-shadow: 0 6px 18px rgba(0,0,0,0.18);
  }
  .card--front { left: 60px; top: 40px; background: var(--card-white); }
  .card--back {
    left: 540px; top: 420px;
    background: radial-gradient(circle at 50% 40%, #3a78aa 0%, #1f5583 35%, #123d63 75%, #0e3456 100%);
  }

  .card__waves { position: absolute; left: 0; top: 0; width: 600px; height: 345px; }

  .brand { position: absolute; left: 36px; top: 40px; display: flex; align-items: center; gap: 12px; }
  .brand__mark { width: 40px; height: 40px; background: var(--mid-blue); border-radius: 6px; }
  .brand__name {
    font-family: "Cinzel", Georgia, serif; font-weight: 700;
    color: var(--brand-green); font-size: 27px; line-height: 1.05; letter-spacing: 0.5px;
    width: 280px;
  }

  .person { position: absolute; left: 420px; top: 44px; font-family: "Tinos", "Times New Roman", serif; color: var(--name-blue); }
  .person__name { font-size: 20px; }
  .person__role { font-size: 13px; margin-top: 1px; }

  .contact { position: absolute; top: 266px; left: 36px; right: 36px; display: flex; color: var(--text-white); font-size: 13px; line-height: 1.55; }
  .contact__address { width: 222px; }
  .contact__divider { width: 1px; height: 40px; background: var(--soft-white); margin: 2px 24px 0 0; }
  .contact__line { display: flex; align-items: center; gap: 10px; }
  .contact__icon { width: 13px; height: 13px; flex: none; }

  .back__mark {
    position: absolute; left: 0; right: 0; top: 118px; text-align: center;
    font-family: "Cinzel", Georgia, serif; font-weight: 700; font-size: 44px;
    color: rgba(255,255,255,0.18); line-height: 1.05;
  }
  .back__web { position: absolute; left: 0; right: 0; bottom: 30px; text-align: center; color: var(--text-white); font-size: 14px; }
</style>
</head>
<body>

<section class="card card--front" aria-label="Business card front">
  <svg class="card__waves" viewBox="0 0 600 345" aria-hidden="true">
    <defs>
      <linearGradient id="greenSwoosh" x1="0" x2="1">
        <stop offset="0" stop-color="#a9cf3c"/>
        <stop offset="0.6" stop-color="#6fb23a"/>
        <stop offset="1" stop-color="#2f8f3c"/>
      </linearGradient>
      <linearGradient id="blueBand" x1="0" y1="0" x2="0" y2="1">
        <stop offset="0" stop-color="#2d6c9e"/>
        <stop offset="1" stop-color="#143f66"/>
      </linearGradient>
    </defs>
    <path d="M0 190 C150 205 320 215 600 140 L600 175 C380 235 170 225 0 215 Z" fill="url(#greenSwoosh)"/>
    <path d="M0 222 C170 235 380 240 600 165 L600 345 L0 345 Z" fill="url(#blueBand)"/>
    <path d="M0 222 C170 235 380 240 600 165" fill="none" stroke="#ffffff" stroke-width="3" opacity="0.7"/>
  </svg>

  <div class="brand">
    <span class="brand__mark"></span>
    <span class="brand__name">BRIGHT PATH CHIROPRACTIC &amp; WELLNESS</span>
  </div>

  <div class="person">
    <p class="person__name">Marcus Hale</p>
    <p class="person__role">Chiropractor</p>
  </div>

  <div class="contact">
    <div class="contact__address">
      <p>812 Orvale Ave, Suite K</p>
      <p>Corbin Falls, Tx. 78245</p>
    </div>
    <span class="contact__divider"></span>
    <div class="contact__details">
      <p class="contact__line">
        <svg class="contact__icon" viewBox="0 0 16 16" aria-hidden="true"><circle cx="8" cy="8" r="7.5" fill="#fff"/><path d="M5 4.2 L6.6 4 L7.3 6 L6.4 6.8 C6.9 8 7.9 9 9.2 9.6 L10 8.7 L12 9.4 L11.8 11 C8 11.2 4.8 8 5 4.2 Z" fill="#1f4f7a"/></svg>
        (830) 555-0147
      </p>
      <p class="contact__line">
        <svg class="contact__icon" viewBox="0 0 16 16" aria-hidden="true"><circle cx="8" cy="8" r="7.5" fill="#fff"/><circle cx="8" cy="8" r="5" fill="none" stroke="#1f4f7a" stroke-width="1"/><path d="M3 8 H13 M8 3 C5.5 6 5.5 10 8 13 M8 3 C10.5 6 10.5 10 8 13" fill="none" stroke="#1f4f7a" stroke-width="1"/></svg>
        www.corbinfallsspine.com
      </p>
    </div>
  </div>
</section>

<section class="card card--back" aria-label="Business card back">
  <p class="back__mark">BRIGHT PATH</p>
  <p class="back__web">www.corbinfallsspine.com</p>
</section>

</body>
</html>
```